WHERE RIVERS LEARN TO SING

Where Rivers Learn To Sing is the title of my book. The book is written to specifically address a major issue the world over which is the ability of think. Educational system in many parts of the world trains us to DO as supposed to Create. In the new world order, doing will always be inferior to thinking. The book is packed with methodologies and case studies. I need a unique design for the book.
Visual of the human brain as part of the creative element / rendition
Since the book is about creative thinking and innovation, I need a creative masterpiece that will be appealing to the eye on the shelf with a strong connection of curiosity & engagement. I personally am of the opinion that visual of the brain is quite off putting
AUTHOR: TUNDE OKORAFOR
PRINTED BY: MERIDIAN LEAF BOOKS
BOOK SIZE: A5

Target Market(s)

Middle to Senior Level Managers in the Private Sector, Fresh Graduates, Entrepreneurs & SME Owners, Government

Font styles to use
Serif

Colors

Designer to choose colors to be used in the design.

Requirements
Must have
• On the front cover, in addition to the title, it should also have the pay off ''Discover & Discover & Unleash The Power Of Your Creative Mind
• Simple back cover design that allows for authors note etc to be very legible
• another must have is space for authors picture
• Front cover Star Burst (WARNING: this book will be difficult to lend)
Should not have
• Visual of the human brain as part of the creative element / rendition

```html
<!DOCTYPE html>
<html lang="en">
<head>
<meta charset="utf-8">
<title>Where Rivers Learn To Sing — Front Cover</title>
<link rel="stylesheet" href="https://fonts.googleapis.com/css2?family=Marcellus&family=Tinos:wght@700&display=swap">
<style>
  :root {
    --page-bg: #e9e8ea;
    --paper: #f6f6f8;
    --ink-navy: #1c2a3a;
    --ink-dark: #222222;
    --stone-dark: #2c3848;
    --stone-mid: #4a5a6c;
    --stone-warm: #8a6a4e;
    --stone-light: #c8b8a2;
    --glow: #f4f1e6;
    --subtitle: #f2f2f2;
    --burst: #ffffff;
  }
  * { box-sizing: border-box; margin: 0; padding: 0; }
  html, body {
    width: 1200px;
    height: 1200px;
    overflow: hidden;
    background: var(--page-bg);
  }
  .cover {
    position: absolute;
    left: 220px;
    top: 62px;
    width: 760px;
    height: 1076px;
    background: var(--paper);
    display: flex;
    flex-direction: column;
    box-shadow: 0 6px 24px rgba(0,0,0,0.18);
  }
  .title-band {
    height: 172px;
    display: flex;
    align-items: center;
    justify-content: center;
    padding: 0 30px;
  }
  .book-title {
    font-family: "Marcellus", serif;
    font-weight: 400;
    font-size: 44px;
    letter-spacing: 1px;
    color: var(--ink-navy);
    text-align: center;
    white-space: nowrap;
  }
  .artwork {
    position: relative;
    flex: 1;
    overflow: hidden;
  }
  .artwork-fill {
    position: absolute;
    inset: 0;
    background:
      radial-gradient(ellipse 26% 24% at 50% 40%, var(--glow) 0%, rgba(244,241,230,0.35) 45%, rgba(244,241,230,0) 100%),
      radial-gradient(ellipse 34% 58% at 50% 60%, var(--stone-light) 0%, var(--stone-warm) 45%, rgba(138,106,78,0) 80%),
      linear-gradient(180deg, var(--stone-mid) 0%, var(--stone-dark) 100%);
  }
  .tagline {
    position: absolute;
    top: 38px;
    left: 0;
    right: 0;
    font-family: "Marcellus", serif;
    font-size: 30px;
    line-height: 1.3;
    color: var(--subtitle);
    text-align: center;
    text-transform: uppercase;
    text-shadow: 0 1px 3px rgba(0,0,0,0.4);
  }
  .warning-burst {
    position: absolute;
    left: 308px;
    top: 590px;
    width: 200px;
    height: 200px;
  }
  .warning-burst svg {
    position: absolute;
    inset: 0;
  }
  .warning-text {
    position: absolute;
    inset: 0;
    display: flex;
    flex-direction: column;
    align-items: center;
    justify-content: center;
    font-family: "Tinos", serif;
    font-weight: 700;
    font-size: 14px;
    line-height: 1.3;
    color: var(--ink-dark);
    text-align: center;
  }
  .author-band {
    height: 108px;
    display: flex;
    align-items: center;
    justify-content: center;
  }
  .author-name {
    font-family: "Marcellus", serif;
    font-size: 26px;
    letter-spacing: 1.5px;
    color: var(--ink-dark);
  }
</style>
</head>
<body>
  <main class="cover">
    <header class="title-band">
      <h1 class="book-title">WHERE RIVERS LEARN TO SING</h1>
    </header>

    <section class="artwork">
      <div class="artwork-fill" role="img" aria-label="Photograph of a dry-stone wall in slate blue, with a head silhouette built from warm brown stacked stones, light glowing through the gaps near the top"></div>

      <p class="tagline">Discover &amp; Discover &amp; Unleash<br>The Power of Your Creative Mind</p>

      <div class="warning-burst">
        <svg viewBox="0 0 200 200" width="200" height="200" aria-hidden="true">
          <polygon fill="var(--burst)" points="100,0 118,62 168,28 140,80 200,96 142,114 176,168 120,138 106,200 90,140 40,176 62,118 0,112 58,88 24,36 82,62"/>
        </svg>
        <div class="warning-text">
          <span>WARNING:</span>
          <span>This book will be</span>
          <span>difficult to lend</span>
        </div>
      </div>
    </section>

    <footer class="author-band">
      <p class="author-name">TUNDE OKORAFOR</p>
    </footer>
  </main>
</body>
</html>
```